Morvelt Promotional Advertisement/Poster

Our company provides financial loans for patients that need help funding their out of pocket deductibles in doctors' offices.  We need a small poster to place in a counter top display that will call attention to our company's offer while not being too large.
The presentation should be user friendly but detailed enough to not be false advertising.
We already have a corporate logo but we need the advertisement quickly.

Target Market(s)
Patients waiting in a professional surgeon's office.
Industry/Entity Type
Financial
Colors
Designer to choose colors to be used in the design.
Requirements
Must have
- Our logo must be present on the page.
Nice to have
- The following are promotional features of our loans:
Interest free loan for the first 60 days.
No down payment required.
No credit checks required.
One year loan term. Instead of having to pay the deductible all at once, we make it possible for a patient to pay their loan with low monthly payments.

```html
<!DOCTYPE html>
<html lang="en">
<head>
<meta charset="UTF-8">
<title>Morvelt Deductible Financing Poster</title>
<link href="https://fonts.googleapis.com/css2?family=Roboto:wght@400;700;900&display=swap" rel="stylesheet">
<style>
  :root {
    --canvas-bg: #ffffff;
    --sheet-bg: #ffffff;
    --sheet-edge: #d6d6d6;
    --brand-blue: #3548a8;
    --tagline-grey: #8a8a8a;
    --box-top: #5f70b2;
    --box-bottom: #2b3a80;
    --box-text: #ffffff;
    --plus: #1b8fc2;
    --footer-text: #3c3c3c;
  }
  * { box-sizing: border-box; margin: 0; padding: 0; }
  html, body {
    width: 1200px;
    height: 1200px;
    overflow: hidden;
    background: var(--canvas-bg);
    font-family: "Roboto", Arial, sans-serif;
  }
  .poster {
    position: absolute;
    left: 186px;
    top: 22px;
    width: 812px;
    height: 1152px;
    background: var(--sheet-bg);
    border: 1px solid var(--sheet-edge);
  }
  .brand {
    position: absolute;
    left: 0;
    right: 0;
    top: 150px;
    text-align: center;
  }
  .brand-name {
    display: inline-flex;
    align-items: center;
    gap: 18px;
    font-size: 88px;
    font-weight: 400;
    color: var(--brand-blue);
    line-height: 1;
  }
  .brand-dot {
    width: 34px;
    height: 34px;
    border-radius: 50%;
    background: var(--brand-blue);
  }
  .tagline {
    margin-top: 8px;
    font-size: 21px;
    letter-spacing: 0.5px;
    color: var(--tagline-grey);
    font-weight: 400;
  }
  .offers {
    position: absolute;
    left: 94px;
    top: 319px;
    width: 621px;
    list-style: none;
  }
  .offer {
    height: 120px;
    border-radius: 7px;
    background: linear-gradient(to bottom, var(--box-top), var(--box-bottom));
    color: var(--box-text);
    font-weight: 700;
    font-size: 36px;
    line-height: 1.4;
    text-align: center;
    display: flex;
    align-items: center;
    justify-content: center;
  }
  .plus {
    height: 67px;
    display: flex;
    align-items: center;
    justify-content: center;
  }
  .plus svg { width: 48px; height: 48px; }
  .offer-last { margin-top: 0; }
  .footer {
    position: absolute;
    left: 0;
    right: 0;
    top: 1048px;
    text-align: center;
    color: var(--footer-text);
    font-weight: 700;
    font-size: 19px;
    line-height: 1.45;
  }
</style>
</head>
<body>
  <main class="poster">
    <header class="brand">
      <div class="brand-name"><span class="brand-dot"></span>Morvelt</div>
      <p class="tagline">AFFORDABLE DEDUCTIBLE FINANCING</p>
    </header>

    <ul class="offers">
      <li class="offer">INTEREST FREE LOAN<br>FOR THE FIRST 60 DAYS</li>
      <li class="plus" aria-hidden="true">
        <svg viewBox="0 0 48 48"><rect x="19" y="3" width="10" height="42" rx="2" fill="var(--plus)"/><rect x="3" y="19" width="42" height="10" rx="2" fill="var(--plus)"/></svg>
      </li>
      <li class="offer">NO DOWN<br>PAYMENT REQUIRED</li>
      <li class="plus" aria-hidden="true">
        <svg viewBox="0 0 48 48"><rect x="19" y="3" width="10" height="42" rx="2" fill="var(--plus)"/><rect x="3" y="19" width="42" height="10" rx="2" fill="var(--plus)"/></svg>
      </li>
      <li class="offer">NO CREDIT<br>CHECKS REQUIRED</li>
      <li class="plus" aria-hidden="true">
        <svg viewBox="0 0 48 48"><rect x="19" y="3" width="10" height="42" rx="2" fill="var(--plus)"/><rect x="3" y="19" width="42" height="10" rx="2" fill="var(--plus)"/></svg>
      </li>
      <li class="offer offer-last">LOW MONTHLY PAYMENTS</li>
    </ul>

    <footer class="footer">
      <p>For more information or to apply</p>
      <p>Call us today on 000-000-00 or visit our website www.website.com</p>
    </footer>
  </main>
</body>
</html>
```